Brookvine Estates Business Card

Business Card:

Somewhere on front of card, please include Broker License Number: 5839261

Website is BrookvineEstates.com

Address is:
7216 Orchardpine Ave E
Saginaw, MI 48517

I'll let you use creative freedom on the rest; we obviously need Name, Title, Email (@BrookvineEstates.com), Office Phone, Cell Phone.

Don't want any special die-cutting, just a standard size business card.

On the back, include a place for the date and time of an appointment to be written in pen.

Industry/Entity Type

Business

Requirements
Must have
• Our logo, attached to email.

```html
<!DOCTYPE html>
<html lang="en">
<head>
<meta charset="UTF-8">
<title>Brookvine Estates Business Card</title>
<link rel="stylesheet" href="https://fonts.googleapis.com/css2?family=Lato:wght@400;700;900&display=swap">
<style>
  :root {
    --navy: #2e2d6e;
    --silver: #b9b9b9;
    --frame: #5f6066;
    --ink: #161616;
    --paper: #ffffff;
  }
  * { margin: 0; padding: 0; box-sizing: border-box; }
  html, body {
    width: 1200px;
    height: 686px;
    overflow: hidden;
    background: var(--paper);
  }
  .card {
    position: relative;
    width: 1200px;
    height: 686px;
    background: var(--paper);
    font-family: "Lato", sans-serif;
    color: var(--ink);
    overflow: hidden;
  }
  .brand-name {
    position: absolute;
    left: 30px;
    top: 104px;
    font-size: 60px;
    font-weight: 700;
    color: var(--navy);
    letter-spacing: -0.5px;
    line-height: 1;
  }
  .address {
    position: absolute;
    left: 29px;
    top: 278px;
    font-size: 29px;
    line-height: 40px;
  }
  .contact-list {
    position: absolute;
    left: 32px;
    top: 383px;
    list-style: none;
    font-size: 29px;
    line-height: 40px;
  }
  .contact-list li {
    display: flex;
    align-items: center;
    height: 40px;
  }
  .contact-icon {
    width: 34px;
    height: 32px;
    margin-right: 20px;
    fill: var(--navy);
    flex-shrink: 0;
  }
  .person {
    position: absolute;
    right: 103px;
    top: 286px;
    text-align: right;
  }
  .person-name {
    font-size: 58px;
    font-weight: 900;
    color: var(--navy);
    line-height: 66px;
    letter-spacing: -0.3px;
  }
  .person-title,
  .person-license {
    font-size: 33px;
    line-height: 46px;
  }
  .side-tab {
    position: absolute;
    left: 1118px;
    top: 289px;
    width: 110px;
    height: 142px;
    background: var(--navy);
    border: 4px solid var(--frame);
    border-radius: 16px;
  }
  .footer-rule {
    position: absolute;
    left: 0;
    top: 594px;
    width: 1200px;
    height: 12px;
    background: var(--silver);
  }
  .footer-band {
    position: absolute;
    left: 0;
    top: 606px;
    width: 1200px;
    height: 80px;
    background: var(--navy);
  }
</style>
</head>
<body>
<main class="card">
  <div class="brand-name">Brookvine Estates</div>

  <address class="address" style="font-style: normal;">
    <div>7216 Orchardpine Ave E</div>
    <div>Saginaw, MI 48517</div>
  </address>

  <ul class="contact-list">
    <li>
      <svg class="contact-icon" viewBox="0 0 34 32" aria-hidden="true">
        <path d="M2 11 C2 5 8 3 17 3 C26 3 32 5 32 11 L32 13 L24 13 L24 9 L10 9 L10 13 L2 13 Z"/>
        <path d="M9 14 L25 14 L30 28 L4 28 Z"/>
        <rect x="12" y="17" width="3" height="2" fill="#fff"/>
        <rect x="16" y="17" width="3" height="2" fill="#fff"/>
        <rect x="20" y="17" width="3" height="2" fill="#fff"/>
        <rect x="11" y="21" width="3" height="2" fill="#fff"/>
        <rect x="16" y="21" width="3" height="2" fill="#fff"/>
        <rect x="21" y="21" width="3" height="2" fill="#fff"/>
      </svg>
      <span>914-555-0182</span>
    </li>
    <li>
      <svg class="contact-icon" viewBox="0 0 34 32" aria-hidden="true">
        <path d="M10 0 H24 A3 3 0 0 1 27 3 V29 A3 3 0 0 1 24 32 H10 A3 3 0 0 1 7 29 V3 A3 3 0 0 1 10 0 Z M10 4 V25 H24 V4 Z"/>
        <circle cx="17" cy="28.5" r="1.6" fill="#fff"/>
      </svg>
      <span>914-555-0247</span>
    </li>
    <li>
      <svg class="contact-icon" viewBox="0 0 34 32" aria-hidden="true">
        <path d="M1 7 H33 L17 19 Z"/>
        <path d="M1 10 L12 18 L1 26 Z"/>
        <path d="M33 10 L22 18 L33 26 Z"/>
        <path d="M14 19.5 L17 22 L20 19.5 L31 27 H3 Z"/>
      </svg>
      <span>marcus@BrookvineEstates.com</span>
    </li>
    <li>
      <svg class="contact-icon" viewBox="0 0 34 32" aria-hidden="true">
        <path d="M1 3 H33 V23 H1 Z M4 6 V20 H30 V6 Z"/>
        <rect x="15" y="23" width="4" height="5"/>
        <rect x="9" y="28" width="16" height="2.5"/>
      </svg>
      <span>BrookvineEstates.com</span>
    </li>
  </ul>

  <div class="person">
    <div class="person-name">Marcus Hale</div>
    <div class="person-title">President</div>
    <div class="person-license">License Number: 5839261</div>
  </div>

  <div class="side-tab"></div>

  <div class="footer-rule"></div>
  <div class="footer-band"></div>
</main>
</body>
</html>
```